Dovanne Luxury Landscapes

A landscape business card.

Target Market(s)

Middle aged and up. Professionals.

Industry/Entity Type

Landscape

Contact Information for Business Card

Waverley

Colors
0054AA
0677BA
7BADD7
CADEEF
E8F1F8
0094D4
00A9DD
6FCCEA
C7EBF8
E9F6FB

Requirements
Must have
• The color blue and silver be very attractive
Nice to have
• An embossed logo. A watermark of a plant or something that indicates that we are a landscape company in the background of the backside where list of services are offered. . List of services on the back.
Should not have
• Red, yellow, orange.

```html
<!DOCTYPE html>
<html lang="en">
<head>
<meta charset="utf-8">
<title>Dovanne Luxury Landscapes – Business Card</title>
<link href="https://fonts.googleapis.com/css2?family=Poppins:wght@400;500;600&family=Marcellus&display=swap" rel="stylesheet">
<style>
  :root{
    --page:#3a3a3c;
    --royal:#2f46a8;
    --royal-deep:#23369a;
    --silver:#c4c8cf;
    --silver-light:#dde0e5;
    --ice:#e8f1f8;
    --white:#ffffff;
    --photo-sky:#4f68bf;
    --photo-foliage:#3b4f9e;
    --photo-bloom:#7d4aa8;
  }
  *{box-sizing:border-box;margin:0;padding:0}
  html,body{width:1200px;height:689px;overflow:hidden;background:var(--page)}
  .canvas{position:relative;width:1200px;height:689px}
  .card{position:absolute;top:190px;width:540px;height:309px;border-radius:16px;overflow:hidden;box-shadow:0 14px 30px rgba(0,0,0,.45)}

  /* Services side */
  .card--services{left:30px;background:var(--royal)}
  .card--services .photo{position:absolute;inset:0;
    background:
      radial-gradient(ellipse 40% 55% at 78% 35%, var(--photo-bloom), transparent 70%),
      radial-gradient(ellipse 60% 50% at 30% 60%, var(--photo-foliage), transparent 75%),
      linear-gradient(180deg,var(--photo-sky) 0%,var(--photo-foliage) 55%,var(--royal-deep) 100%);}
  .card--services .brand{position:absolute;left:0;right:0;top:70px;text-align:center;color:var(--ice)}
  .brand-name{font-family:"Poppins",sans-serif;font-weight:500;font-size:46px;letter-spacing:6px;line-height:1}
  .brand-tag{font-family:"Poppins",sans-serif;font-weight:400;font-size:14px;letter-spacing:5px;margin-top:8px;text-transform:uppercase}
  .services{position:absolute;left:0;right:0;bottom:44px;text-align:center;color:var(--white);
    font-family:"Poppins",sans-serif;font-size:12.5px;letter-spacing:.6px;line-height:1.6;text-transform:uppercase}

  /* Contact side */
  .card--contact{left:630px;background:var(--royal)}
  .card--contact .silver-panel{position:absolute;inset:0;width:540px;height:309px}
  .card--contact .mark-name{position:absolute;left:40px;top:108px;font-family:"Poppins",sans-serif;font-weight:600;
    font-size:44px;color:var(--royal);letter-spacing:2px}
  .tagline{position:absolute;left:22px;bottom:22px;font-family:"Poppins",sans-serif;font-weight:600;font-size:13.5px;
    letter-spacing:.8px;color:var(--royal);text-transform:uppercase}
  .contact{position:absolute;right:26px;top:34px;text-align:right;color:var(--white);font-family:"Poppins",sans-serif}
  .person{font-family:"Marcellus",serif;font-size:21px;letter-spacing:.5px;text-transform:uppercase;font-weight:400}
  .role{font-size:12.5px;margin-top:2px}
  .rule{width:44px;height:1.5px;background:var(--white);margin:10px 0 10px auto}
  .line{font-size:13px;line-height:1.5;display:flex;justify-content:flex-end;align-items:center;gap:6px}
  .line svg{width:12px;height:12px}
  .address{font-size:13px;line-height:1.45}
</style>
</head>
<body>
<main class="canvas">

  <section class="card card--services">
    <div class="photo" role="img" aria-label="Photograph of a landscaped garden with trees, flowering shrubs and a lamp post, tinted blue"></div>
    <div class="brand">
      <div class="brand-name">DOVANNE</div>
      <div class="brand-tag">Luxury Landscapes</div>
    </div>
    <p class="services">
      Decks • Pools • Garden Install and Cleanup • Retaining Walls<br>
      Pergolas • Interlock Stone • Outdoor Lighting<br>
      Landscape Consultations • Auto Mower Installs
    </p>
  </section>

  <section class="card card--contact">
    <svg class="silver-panel" viewBox="0 0 540 309" aria-hidden="true">
      <path d="M0 309 L0 70 C50 20 200 0 270 28 C320 50 312 170 300 232 C380 236 470 242 540 252 L540 309 Z" fill="var(--silver)"/>
      <path d="M0 70 C50 20 200 0 270 28 C320 50 312 170 300 232 C380 236 470 242 540 252" fill="none" stroke="var(--silver-light)" stroke-width="3"/>
    </svg>
    <div class="mark-name">Dovanne</div>
    <div class="tagline">Luxury Landscape Professionals</div>
    <div class="contact">
      <div class="person">Marla Quennell</div>
      <div class="role">RSE Horticulturist</div>
      <div class="rule"></div>
      <div class="line">902-555-LAWN
        <svg viewBox="0 0 24 24" aria-hidden="true"><path fill="var(--white)" d="M6.6 10.8a15 15 0 006.6 6.6l2.2-2.2a1 1 0 011-.25 11.4 11.4 0 003.6.57 1 1 0 011 1V20a1 1 0 01-1 1A17 17 0 013 4a1 1 0 011-1h3.5a1 1 0 011 1c0 1.25.2 2.45.57 3.57a1 1 0 01-.25 1z"/></svg>
      </div>
      <div class="line">www.dovanne.com
        <svg viewBox="0 0 24 24" aria-hidden="true"><circle cx="12" cy="12" r="9.5" fill="none" stroke="var(--white)" stroke-width="2"/><path d="M2.5 12h19M12 2.5c3 3 3 16 0 19M12 2.5c-3 3-3 16 0 19" fill="none" stroke="var(--white)" stroke-width="1.6"/></svg>
      </div>
      <div class="rule"></div>
      <div class="address">18B Hollis Glen Road<br>Waverley, Nova Scotia<br>B0X 2K7</div>
    </div>
  </section>

</main>
</body>
</html>
```